Business Card Design - Ember Hill Lodge

We are looking at a new design for our business cards that has a modern and professional look. We run a residential aged care facility focussing on the care of residents. The cards will be used for potential clients, consultants and business opportunities in this sector. Blue and white is our main colours and would to see these colours incorporated in the design.
Industry/Entity Type
Business
Contact Information for Business Card
Ember Hill Lodge, Dean Marsh, dmarsh@emberhilllodge-mail.example, Finance Manager, 0491 372 608, BCom, 27 Marbury Way, Ashford Vale, Qld 4190.
Look and feel

```html
<!DOCTYPE html>
<html lang="en">
<head>
<meta charset="utf-8">
<title>Ember Hill Lodge – Business Card</title>
<link rel="stylesheet" href="https://fonts.googleapis.com/css2?family=Open+Sans:wght@400;600;700&display=swap">
<style>
  :root {
    --page-bg: #e4e4e2;
    --card-white: #ffffff;
    --card-shade: #ececec;
    --brand-blue: #4d7d97;
    --brand-blue-dark: #3d6a83;
    --accent-taupe: #a59d96;
    --text-grey: #4f4f4f;
    --rule-grey: #cfcfcf;
  }
  * { margin: 0; padding: 0; box-sizing: border-box; }
  html, body {
    width: 1200px;
    height: 950px;
    overflow: hidden;
    background: var(--page-bg);
    font-family: "Open Sans", Arial, sans-serif;
  }
  .card {
    position: absolute;
    left: 100px;
    top: 190px;
    width: 1000px;
    height: 570px;
    border-radius: 28px;
    overflow: hidden;
    background: linear-gradient(160deg, var(--card-white) 40%, var(--card-shade) 100%);
    box-shadow: 0 10px 30px rgba(0,0,0,0.18);
  }
  .card-waves {
    position: absolute;
    left: 0;
    top: 0;
    width: 1000px;
    height: 570px;
  }
  .brand {
    position: absolute;
    left: 50px;
    top: 172px;
    width: 380px;
    display: flex;
    align-items: center;
    gap: 14px;
  }
  .brand-dot {
    width: 30px;
    height: 30px;
    border-radius: 50%;
    background: var(--brand-blue);
    flex: none;
  }
  .brand-name {
    font-size: 31px;
    font-weight: 600;
    color: var(--brand-blue);
    letter-spacing: 0.5px;
    white-space: nowrap;
  }
  .divider {
    position: absolute;
    left: 455px;
    top: 95px;
    width: 2px;
    height: 270px;
    background: var(--rule-grey);
  }
  .contact {
    position: absolute;
    left: 488px;
    top: 92px;
    width: 490px;
    color: var(--text-grey);
  }
  .contact-name {
    font-size: 32px;
    font-weight: 700;
    color: var(--brand-blue);
    line-height: 1.15;
  }
  .contact-name .credential { font-size: 22px; }
  .contact-role {
    font-size: 22px;
    color: var(--accent-taupe);
    margin-bottom: 14px;
  }
  .contact-address {
    font-size: 22px;
    line-height: 1.35;
    margin-bottom: 6px;
  }
  .contact-line {
    display: flex;
    align-items: center;
    gap: 12px;
    font-size: 22px;
    line-height: 1.5;
    white-space: nowrap;
  }
  .contact-icon { width: 20px; height: 20px; flex: none; }
</style>
</head>
<body>
  <div class="card">
    <svg class="card-waves" viewBox="0 0 1000 570" aria-hidden="true">
      <path d="M0 380 C 250 420, 520 490, 1000 430 L1000 455 C 520 515, 250 445, 0 408 Z" fill="var(--accent-taupe)"/>
      <path d="M0 400 C 250 445, 520 520, 1000 460 L1000 570 L0 570 Z" fill="var(--brand-blue)"/>
      <path d="M0 470 C 300 520, 600 560, 1000 500 L1000 570 L0 570 Z" fill="var(--brand-blue-dark)" opacity="0.35"/>
    </svg>

    <div class="brand">
      <span class="brand-dot"></span>
      <span class="brand-name">EMBER HILL LODGE</span>
    </div>

    <div class="divider"></div>

    <div class="contact">
      <p class="contact-name">Dean Marsh <span class="credential">BCom</span></p>
      <p class="contact-role">Finance Manager</p>
      <p class="contact-address">27 Marbury Way<br>Ashford Vale, Qld 4190.</p>
      <p class="contact-line">
        <svg class="contact-icon" viewBox="0 0 24 24"><path fill="var(--brand-blue)" d="M6.6 10.8a15 15 0 0 0 6.6 6.6l2.2-2.2c.3-.3.7-.4 1-.2 1.1.4 2.3.6 3.6.6.6 0 1 .4 1 1V20c0 .6-.4 1-1 1A17 17 0 0 1 3 4c0-.6.4-1 1-1h3.5c.6 0 1 .4 1 1 0 1.3.2 2.5.6 3.6.1.3 0 .7-.2 1z"/></svg>
        0491 372 608
      </p>
      <p class="contact-line">
        <svg class="contact-icon" viewBox="0 0 24 24"><rect x="2" y="5" width="20" height="14" rx="2" fill="var(--brand-blue)"/><path d="M3 6l9 7 9-7" fill="none" stroke="#fff" stroke-width="1.6"/></svg>
        dmarsh@emberhilllodge-mail.example
      </p>
      <p class="contact-line">
        <svg class="contact-icon" viewBox="0 0 24 24"><circle cx="12" cy="12" r="10" fill="var(--brand-blue)"/><path d="M8 12l3 3 5-6" fill="none" stroke="#fff" stroke-width="2"/></svg>
        www.emberhilllodge.example
      </p>
    </div>
  </div>
</body>
</html>
```